Business Card Design Project

I need a business card design for an Organic drive thru coffee kiosk. We will serve organic coffee, teas & smoothies and will serve healthy breakfast food/snacks for people on the go.
I want the card to have 2-3 colors max (earthy colors like browns, greens and so on).
I have attached the logo I want used and would love to play off the theme of "balance."
Include:
Tidy-Kettle Coffee
address: 4820 Gorvin Ct. Raleigh, NC 27583
phone: 919-731-4062
website: www.tidy-kettle.com (website is not up yet but still include it on card)
email: Rosalind@tidy-kettle.com
I want one of the following sayings somewhere on the card (the front or back is fine):
"Eat & Drink Well, on the run!"
"Break the fast with Tidy-Kettle"
Maybe on the back list what we offer:
-Organic coffee, espresso & tea
-Blendora smoothies & protein shakes
-Zesty Pour (100% fresh local fruit and veggies)
-Tender Nibs

```html
<!DOCTYPE html>
<html lang="en">
<head>
<meta charset="utf-8">
<title>Tidy-Kettle Coffee — Business Card</title>
<link rel="stylesheet" href="https://fonts.googleapis.com/css2?family=Source+Sans+3:wght@400;600;700&display=swap">
<style>
  :root {
    --stage: #e6e6e6;
    --leaf: #44622f;
    --roast: #795433;
    --roast-soft: #8c6443;
    --sprout: #7dc25a;
    --sprout-pale: #8fc96c;
    --clay: #c88a55;
    --espresso: #4a3228;
    --bean: #5c3328;
  }
  * { box-sizing: border-box; margin: 0; padding: 0; }
  html, body {
    width: 1200px; height: 849px; overflow: hidden;
    background: var(--stage);
    font-family: "Source Sans 3", sans-serif;
  }
  .canvas { position: relative; width: 1200px; height: 849px; }
  .card { position: absolute; top: 78px; width: 400px; height: 700px; text-align: center; overflow: hidden; }
  .card--back { left: 133px; background: var(--leaf); }
  .card--front { left: 675px; background: var(--roast); }

  .back-name {
    position: absolute; top: 196px; left: 0; right: 0;
    font-size: 42px; font-weight: 600; color: var(--bean);
  }
  .offer-list { position: absolute; top: 414px; left: 0; right: 0; list-style: none; }
  .offer-list li { font-size: 16px; color: var(--sprout-pale); height: 40px; line-height: 22px; }
  .website {
    position: absolute; top: 654px; left: 0; right: 0;
    font-size: 19px; color: var(--clay); letter-spacing: 0.3px;
  }

  .holder {
    position: absolute; top: 28px; left: 0; right: 0;
    font-size: 22px; font-weight: 700; color: var(--sprout);
  }
  .brand-disc {
    position: absolute; left: 78px; top: 140px; width: 250px; height: 250px;
    border-radius: 50%; background: var(--roast-soft);
  }
  .brand-name {
    position: absolute; top: 228px; left: 0; right: 0;
    font-size: 50px; font-weight: 400; color: var(--espresso); letter-spacing: -0.5px;
  }
  .brand-tagline {
    position: absolute; top: 300px; left: 0; right: 0;
    font-size: 13px; font-weight: 600; color: var(--sprout); letter-spacing: 3px;
  }
  .company {
    position: absolute; top: 444px; left: 0; right: 0;
    font-size: 28px; font-weight: 600; color: var(--sprout);
  }
  .address {
    position: absolute; top: 484px; left: 0; right: 0;
    font-size: 16px; line-height: 20px; color: var(--clay); font-style: normal;
  }
  .contact {
    position: absolute; top: 564px; left: 0; right: 0;
    font-size: 16px; line-height: 20px; color: var(--clay);
  }
  .motto {
    position: absolute; left: 0; right: 0; bottom: 0; height: 64px;
    background: var(--leaf); padding-top: 8px;
    font-size: 15.5px; line-height: 20px; color: var(--sprout-pale);
  }
</style>
</head>
<body>
<main class="canvas">
  <section class="card card--back">
    <p class="back-name">Tidy-Kettle</p>
    <ul class="offer-list">
      <li>Organic Coffee, espresso &amp; tea</li>
      <li>Blendora smoothies &amp; protein shakes</li>
      <li>Zesty Pour (100% local fruit &amp; veggies)</li>
      <li>Tender Nibs</li>
    </ul>
    <p class="website">www.tidy-kettle.com</p>
  </section>

  <section class="card card--front">
    <p class="holder">Rosalind</p>
    <div class="brand-disc"></div>
    <p class="brand-name">Tidy-Kettle</p>
    <p class="brand-tagline">ORGANIC COFFEE + CAFE</p>
    <h1 class="company">Tidy-Kettle Coffee</h1>
    <address class="address">4820 Gorvin Ct. Raleigh<br>NC 27583</address>
    <p class="contact">919-731-4062<br>Rosalind@tidy-kettle.com</p>
    <p class="motto">Eat and drink well, on the run!.<br>Break the fast, with Tidy-Kettle</p>
  </section>
</main>
</body>
</html>
```